基本レイアウトについては
https://zumelo.com/diagrams/XR8k21pTbvNDWfeL
もしくは、添付データのワイヤーをご参照ください。
レイアウトについては必ずしも上記に準じている必要はありません。
ご自由にご提案いただいても結構です。

全体の雰囲気としては
http://www.tomirei-wedding.net/
http://www.hokumorisanjingu.or.jp/
のような、桜色をつかいながら
あまり古臭くなり過ぎないようにアピールできればと思います。

また、製品は
http://www.seiryu-kojin.co.jp/goods/luvasystem
http://www.gw-tmr.co.jp/
のものを使用しています。

美容室へ来られる方は、近隣の方が多く、
和髪以外での競争力はあまりないため、WEB上では
美容師への和髪の講習などの訴求時に、
信頼性を高めるような用途が多くなりそうです。

そのため、上記参考サイトのような
ちょっとしたスタイリッシュさを目指しています。
http://qrvmd.ozu.ne.jp/0597214483/index.html
ホワイト、桜色をベースに、落ち着いた印象に出来ればと存じます。
素材については、
下記URLよりダウンロードしたものをご利用いただければ幸甚です。
http://plumvault.jp/download/a4f19e02bd7753c6e1088f2d94ab37c51e0d2a96

こちらだけですと、制作が難しいと思いますので
http://mobre.jp/
などから、5000円程度までならこちらにて購入可能です。カンプデータにて作成頂き、
納品時に当方にて購入したデータに差し替えていただければと存じます。

【参考サイト】
↑色合い、印象が気に入っています

http://www.gw-tmr.co.jp/
↑使用している製品のホームページです

http://basement-parts.com/2012/166.html
http://basement-parts.com/2011/115.html
↑フッター部分の参照です

基本レイアウト
については、必ずしも忠実である必要はありません。

是非ご提案お待ちしております。
何卒よろしくお願いいたします。

クライアント様との協議の結果こちらの案を採用させていただきました。
上品さと柔らかさのバランスがとてもよく、
視認性も高く、要望を全て満たしておりましたので
こちらの案を採用いたしました。

この度は多数ご提案いただきありがとうございました。
当選に至らなかったランサー様におかれましては大変心苦しいのですが、
またの機会にぜひご提案いただければ幸甚です。
引き続き何卒よろしくお願いいたします。

```html
<!DOCTYPE html>
<html lang="ja">
<head>
<meta charset="utf-8">
<title>ソヨカ美容室</title>
<link href="https://fonts.googleapis.com/css2?family=Noto+Sans+JP:wght@400;500;700&family=Noto+Serif+JP:wght@500&display=swap" rel="stylesheet">
<style>
:root{
  --pink:#d7668c;
  --pink-soft:#f6dbe4;
  --crimson:#a52a3c;
  --ink:#444;
  --muted:#777;
  --line:#d8d8d8;
  --page:#f4f4f4;
  --panel:#fff;
  --foot:#dcdcdc;
  --foot-bar:#8c8388;
}
*{box-sizing:border-box;margin:0;padding:0}
html,body{width:769px;height:1200px;overflow:hidden}
body{background:var(--page);font-family:"Noto Sans JP",sans-serif;color:var(--ink);font-size:11px;position:relative}
.site-header{height:80px;background:var(--panel);position:relative}
.brand{position:absolute;left:14px;top:22px;display:flex;align-items:center;gap:8px}
.brand-dot{width:26px;height:26px;border-radius:50%;background:var(--pink)}
.brand-name{font-family:"Noto Serif JP",serif;font-weight:500;font-size:24px;color:var(--pink);letter-spacing:1px}
.header-info{position:absolute;right:14px;top:14px;font-size:9px;line-height:1.6;color:var(--ink)}
.global-nav{height:38px;margin-top:6px;background:var(--panel);border-top:1px solid var(--line);border-bottom:1px solid var(--line);display:flex;justify-content:center;align-items:center;font-size:12px}
.global-nav a{color:var(--ink);text-decoration:none;padding:0 9px;border-left:1px solid #999}
.global-nav a:first-child{border-left:none}
.hero{position:absolute;top:128px;left:0;width:769px;height:244px;background:linear-gradient(180deg,#7fb6e2 0%,#bcdaf0 45%,#6f8f4c 75%,#4e6a32 100%)}
.hero-figure{position:absolute;right:70px;top:0;width:210px;height:244px;background:linear-gradient(180deg,#3a2a30,#5a2a46 55%,#3b3570)}
.hero-caption{position:absolute;left:120px;top:132px;color:#fff;font-size:14px;letter-spacing:1px;text-shadow:0 1px 2px rgba(0,0,0,.4)}
.sidebar{position:absolute;left:8px;top:390px;width:197px}
.hours-card{height:136px;background:var(--crimson);position:relative;color:#fff}
.hours-card p{position:absolute;left:34px;top:20px;font-size:9px;line-height:1.9}
.hours-tel{position:absolute;left:8px;right:8px;bottom:8px;height:26px;background:#fff;display:flex;align-items:center;justify-content:center;gap:6px;color:var(--crimson);font-weight:700;font-size:16px}
.side-nav{margin-top:17px;list-style:none;background:var(--panel)}
.side-nav li{height:39px;border-bottom:1px solid var(--line);display:flex;align-items:center;padding-left:14px;font-size:11px;position:relative}
.side-nav li.current{background:var(--pink-soft);color:var(--pink)}
.side-nav li.current::before{content:"";position:absolute;left:0;top:0;bottom:0;width:4px;background:var(--pink)}
.lesson-banner{margin-top:14px;height:190px;background:linear-gradient(160deg,#2a2a2e,#4a3d44 60%,#262428);position:relative}
.lesson-banner span{position:absolute;left:0;right:0;bottom:40px;text-align:center;color:#fff;font-size:12px}
.lesson-note{margin-top:8px;font-size:9px;line-height:1.7;color:var(--muted);padding:0 6px}
.content{position:absolute;left:218px;top:390px;width:543px}
.news{background:var(--panel);border:1px solid var(--line);height:205px}
.section-title{font-family:"Noto Serif JP",serif;font-weight:500;font-size:16px;color:var(--ink);padding:12px 14px;border-bottom:1px solid var(--line)}
.news ul{list-style:none;padding:14px 14px 0 38px}
.news li{font-size:11px;line-height:2.05}
.news time{margin-right:16px}
.welcome{margin-top:44px;background:var(--panel);border:1px solid var(--line);height:372px;position:relative}
.welcome-body{position:absolute;left:14px;top:60px;width:262px;font-size:11px;line-height:1.95}
.welcome-body p{margin-bottom:20px}
.storefront{position:absolute;right:20px;top:60px;width:232px;height:198px;background:linear-gradient(180deg,#cfd6cf,#6f8a6a 55%,#3f5a3c)}
.site-footer{position:absolute;left:0;top:1025px;width:769px;height:149px;background:var(--foot)}
.footer-brand{position:absolute;left:14px;top:16px}
.footer-brand .brand-name{font-size:20px;color:var(--ink)}
.footer-info{position:absolute;left:14px;top:54px;font-size:9px;line-height:1.7}
.footer-links{position:absolute;top:14px;list-style:none;font-size:11px;line-height:1.7;border-left:1px solid #aaa;padding-left:8px}
.footer-links.col-a{left:262px}
.footer-links.col-b{left:402px}
.copyright{position:absolute;left:0;top:1174px;width:769px;height:26px;background:var(--foot-bar);color:#fff;font-size:10px;display:flex;align-items:center;justify-content:center}
</style>
</head>
<body>
<header class="site-header">
  <div class="brand"><span class="brand-dot"></span><span class="brand-name">ソヨカ美容室</span></div>
  <div class="header-info">
    電話番号：046-214-4830【要予約】<br>
    営業時間　9:00〜19:00（毎週火曜・第1,3水曜定休）<br>
    神奈川県青葉市若宮町2-23-3
  </div>
</header>
<nav class="global-nav">
  <a href="#">HOME</a><a href="#">メニュー・料金</a><a href="#">製品へのこだわり</a><a href="#">よくある質問</a><a href="#">店舗案内</a>
</nav>
<section class="hero" role="img" aria-label="青空と山並みを背景に、和髪と着物姿の女性とヘアケア製品">
  <div class="hero-figure"></div>
  <p class="hero-caption">環境と身体にやさしい製品を使用している、和髪・着付けもできる美容室です。</p>
</section>
<aside class="sidebar">
  <div class="hours-card">
    <p>営業日　火曜・第1,3水曜定休<br>臨時休業あり<br>お電話でご予約ください</p>
    <div class="hours-tel">
      <svg width="16" height="16" viewBox="0 0 24 24"><path fill="currentColor" d="M6.6 10.8a15 15 0 0 0 6.6 6.6l2.2-2.2c.3-.3.7-.4 1-.2 1.1.4 2.3.6 3.6.6.6 0 1 .4 1 1V20c0 .6-.4 1-1 1C10.6 21 3 13.4 3 4c0-.6.4-1 1-1h3.5c.6 0 1 .4 1 1 0 1.3.2 2.5.6 3.6.1.3 0 .7-.2 1z"/></svg>
      046-214-4830
    </div>
  </div>
  <ul class="side-nav">
    <li class="current">HOME</li><li>メニュー・料金</li><li>製品へのこだわり</li><li>和髪について</li><li>よくある質問</li><li>店舗案内</li>
  </ul>
  <div class="lesson-banner" role="img" aria-label="和髪を結った後ろ姿の写真"><span>和髪について学びませんか？</span></div>
  <p class="lesson-note">技術者向けに、和髪の講習を行っております。詳細をお知らせいたします。</p>
</aside>
<main class="content">
  <section class="news">
    <h2 class="section-title">新着情報</h2>
    <ul>
      <li><time>2014年1月01日</time>新着情報タイトル新着情報タイトル</li>
      <li><time>2014年1月01日</time>新着情報タイトル新着情報タイトル</li>
      <li><time>2014年1月01日</time>新着情報タイトル新着情報タイトル</li>
      <li><time>2014年1月01日</time>新着情報タイトル新着情報タイトル</li>
      <li><time>2014年1月01日</time>新着情報タイトル新着情報タイトル</li>
    </ul>
  </section>
  <section class="welcome">
    <h2 class="section-title">ソヨカ美容室へようこそ</h2>
    <div class="welcome-body">
      <p>ソヨカ美容室は、ミズハ商品やサクラノ商品を始め、環境に優しい製品を厳選し、お客様に使用させて頂いています。環境への配慮も忘れず、化学物質を極力控えて、人にも自然にも優しい美容室を心がけております。</p>
      <p>また、今ではめずらしくなってきた、和髪・着付けに対応した美容室であり、お正月などには多くのご家族が記念撮影をされるためにご来店されます。</p>
      <p>最新の施設ではありませんが、長年培ってきた技術と経験を活かして、お客様との触れ合いを大切に営業しております。是非一度ご来店ください。</p>
    </div>
    <div class="storefront" role="img" aria-label="緑の看板がある美容室の店舗外観"></div>
  </section>
</main>
<footer class="site-footer">
  <div class="footer-brand brand"><span class="brand-dot"></span><span class="brand-name">ソヨカ美容室</span></div>
  <p class="footer-info">電話番号：046-214-4830【要予約】<br>営業時間　9:00〜19:00（火曜・第1,3水曜定休）<br>神奈川県青葉市若宮町2-23-3</p>
  <ul class="footer-links col-a"><li>HOME</li><li>メニュー・料金</li><li>製品へのこだわり</li><li>和髪について</li></ul>
  <ul class="footer-links col-b"><li>よくある質問</li><li>店舗案内</li><li>プライバシーポリシー</li><li>サイトマップ</li></ul>
</footer>
<div class="copyright">Copyright(c)2014 ソヨカ美容室　All Rights Reserved.</div>
</body>
</html>
```